Vodka label for New Brand called KIRO Vodka

We need a label measuring 3.5 inches wide & 5 inches tall for this vodka bottle. The brand is "KIRO Vodka". This should be the largest font on the label. "Handcrafted in the USA" should be on bottle in small font near the bottom. The tagline "Keeping It Real Onward" also needs to be included anywhere that makes sense in a smaller font than the brand name. Also in smaller font at the bottom/corners- "80 proof, 750 ml, 40% alc/vol" I value the human mind over AI, but am providing a couple designs that were AI generated to give you a better idea where to start and what we are looking for. Thank you!

Target Market(s)

21-45 year olds.

Industry/Entity Type

Alcohol

Colors
0054AA
0677BA
7BADD7
CADEEF
E8F1F8
EB3D1F
EC4F4E
F09395
F8D3D4
FCEDEE

Requirements
Should not have
• You can not use the US flag but can use elements of it.

```html
<!DOCTYPE html>
<html lang="en">
<head>
<meta charset="utf-8">
<title>KIRO Vodka – Bottle Label</title>
<link rel="stylesheet" href="https://fonts.googleapis.com/css2?family=Marcellus&family=Roboto+Condensed:wght@700&display=swap">
<style>
  :root {
    --wood-dark: #4a2412;
    --wood-mid: #8a4a22;
    --wood-light: #d99a5a;
    --label-ink: #4a4a40;
    --label-cream: #f7f5e6;
    --art-tone: #e4e0cc;
    --pattern-tone: #ebe8d8;
    --text-black: #111111;
  }
  html, body {
    margin: 0;
    padding: 0;
    width: 700px;
    height: 1200px;
    overflow: hidden;
  }
  .canvas {
    position: relative;
    width: 700px;
    height: 1200px;
    background:
      radial-gradient(ellipse 45% 18% at 50% 0%, rgba(240,180,110,0.85), rgba(240,180,110,0) 100%),
      linear-gradient(90deg, var(--wood-dark) 0%, var(--wood-mid) 30%, #a25c2c 50%, var(--wood-mid) 70%, var(--wood-dark) 100%);
  }
  .label { display: block; }
  .label-outer { fill: var(--label-ink); }
  .label-inner { fill: var(--label-cream); }
  .frame-line { fill: none; stroke: var(--label-ink); stroke-width: 5; }
  .rule { stroke: var(--label-ink); stroke-width: 5; }
  .name-band { fill: var(--label-ink); }
  .name-band-line { fill: none; stroke: var(--label-cream); stroke-width: 4; }
  .glasses-art { fill: var(--art-tone); }
  .pattern-band { fill: var(--pattern-tone); }
  .tagline, .origin, .brand-name {
    font-family: "Marcellus", "Optima", sans-serif;
  }
  .tagline { font-size: 44px; fill: var(--text-black); text-anchor: middle; }
  .brand-name { fill: var(--label-cream); text-anchor: middle; }
  .brand-name-main { font-size: 210px; }
  .brand-name-sub { font-size: 190px; }
  .spec-table { fill: none; stroke: var(--label-ink); stroke-width: 4; }
  .spec-divider { stroke: var(--label-ink); stroke-width: 5; }
  .spec-text {
    font-family: "Roboto Condensed", "Arial Narrow", sans-serif;
    font-weight: 700;
    font-size: 34px;
    fill: var(--label-ink);
  }
  .origin { font-size: 31px; fill: var(--text-black); text-anchor: middle; letter-spacing: 0.5px; }
</style>
</head>
<body>
<div class="canvas">
  <svg class="label" width="700" height="1200" viewBox="0 0 1127 1932" xmlns="http://www.w3.org/2000/svg">
    <path class="label-outer" d="M385 165 C420 110 480 88 563 88 C646 88 706 110 741 165 L895 165 L895 240 L957 240 L957 745 C1005 800 1022 900 1022 962 C1022 1030 1003 1120 957 1180 L957 1660 L895 1660 L895 1765 L741 1765 C706 1820 646 1845 563 1845 C480 1845 420 1820 385 1765 L232 1765 L232 1660 L170 1660 L170 1180 C124 1120 105 1030 105 962 C105 900 122 800 170 745 L170 240 L232 240 L232 165 Z"/>
    <path class="label-inner" d="M410 197 C444 146 495 120 563 120 C631 120 682 146 716 197 L866 197 L866 270 L928 270 L928 742 C972 800 992 900 992 962 C992 1030 972 1120 928 1183 L928 1632 L866 1632 L866 1735 L716 1735 C682 1786 631 1812 563 1812 C495 1812 444 1786 410 1735 L261 1735 L261 1632 L199 1632 L199 1183 C155 1120 135 1030 135 962 C135 900 155 800 199 742 L199 270 L261 270 L261 197 Z"/>

    <path class="frame-line" d="M258 325 L325 325 L325 250 L425 250 C458 205 505 182 563 182 C621 182 668 205 701 250 L805 250 L805 325 L868 325"/>
    <path class="frame-line" d="M207 290 L207 745 M920 290 L920 745 M207 1185 L207 1645 M920 1185 L920 1645"/>
    <path class="frame-line" d="M258 1605 L325 1605 L325 1680 L425 1680 C458 1725 505 1750 563 1750 C621 1750 668 1725 701 1680 L805 1680 L805 1605 L868 1605"/>

    <rect class="glasses-art" x="340" y="265" width="452" height="238" rx="6" role="img" aria-label="Line drawing of three vodka glasses, a tall one between two short ones"/>

    <line class="rule" x1="413" y1="539" x2="715" y2="539"/>
    <line class="rule" x1="322" y1="561" x2="806" y2="561"/>
    <line class="rule" x1="413" y1="583" x2="715" y2="583"/>

    <text class="tagline" x="566" y="652">Keeping It Real Onward</text>

    <rect class="pattern-band" x="262" y="680" width="604" height="44" role="img" aria-label="Faint chevron ornament band"/>

    <path class="name-band" d="M226 745 L900 745 C950 805 972 900 972 965 C972 1040 950 1120 900 1185 L226 1185 C177 1120 155 1040 155 965 C155 900 177 805 226 745 Z"/>
    <path class="name-band-line" d="M240 778 L888 778 C926 832 942 900 942 965 C942 1035 926 1100 888 1154 L240 1154 C201 1100 186 1035 186 965 C186 900 201 832 240 778 Z"/>

    <text class="brand-name brand-name-main" x="566" y="950">KIRO</text>
    <text class="brand-name brand-name-sub" x="604" y="1125">Vodka</text>

    <rect class="pattern-band" x="262" y="1208" width="604" height="44" role="img" aria-label="Faint chevron ornament band"/>

    <line class="rule" x1="413" y1="1280" x2="715" y2="1280"/>
    <line class="rule" x1="322" y1="1302" x2="806" y2="1302"/>
    <line class="rule" x1="413" y1="1324" x2="715" y2="1324"/>

    <rect class="spec-table" x="264" y="1348" width="602" height="222"/>
    <line class="spec-divider" x1="567" y1="1368" x2="567" y2="1550"/>
    <line class="spec-divider" x1="268" y1="1459" x2="836" y2="1459"/>
    <text class="spec-text" x="298" y="1428">PROOF</text>
    <text class="spec-text" x="425" y="1428">80</text>
    <text class="spec-text" x="595" y="1428">ALC./VOL</text>
    <text class="spec-text" x="756" y="1428">40%</text>
    <text class="spec-text" x="298" y="1518">YEAR</text>
    <text class="spec-text" x="425" y="1518">2025</text>
    <text class="spec-text" x="595" y="1518">ML</text>
    <text class="spec-text" x="756" y="1518">750</text>

    <text class="origin" x="563" y="1640">HANDCRAFTED IN THE USA</text>
  </svg>
</div>
</body>
</html>
```